Computer Service Provider in Need of New Letterhead Design

We are Quarrybell Computer Services, a computer/IT services company that provides IT Support, software, hardware, virus monitoring, etc. in Vermont. We are looking for new letterhead, that is both professional and matches the current theme of our business cards & website.
Please note that we want to include the following information:
www.Quarrybell.example
802-555-0147
47 Fernhollow Road, Alderbrook, VT 05999
Proactive Solutions • Approachable People • Proven Performance
I will be attaching our logo along with the business card images.
We would love to have the

```html
<!DOCTYPE html>
<html lang="en">
<head>
<meta charset="utf-8">
<title>Quarrybell Computer Services – Letterhead</title>
<link href="https://fonts.googleapis.com/css2?family=Source+Sans+3:wght@400;700&family=Arimo:wght@700&family=Roboto:wght@400;700&family=Roboto+Condensed:wght@400&family=Lustria&display=swap" rel="stylesheet">
<style>
  :root {
    --backdrop: #e8e8e8;
    --paper: #f5f5f5;
    --navy: #285a82;
    --orange: #f7a23b;
    --text: #555555;
    --heading: #444444;
    --ink: #222222;
    --divider: #f0c48a;
  }
  * { margin: 0; padding: 0; box-sizing: border-box; }
  html, body { width: 1120px; height: 1200px; overflow: hidden; background: var(--backdrop); }
  .sheet {
    position: absolute; left: 200px; top: 92px; width: 720px; height: 1018px;
    background: var(--paper); box-shadow: 0 2px 8px rgba(0,0,0,0.12); overflow: hidden;
  }
  .header-wave { position: absolute; left: 0; top: 0; width: 720px; height: 60px; }
  .brand { position: absolute; left: 54px; top: 52px; display: flex; align-items: center; gap: 10px; }
  .brand-square { width: 44px; height: 44px; background: var(--navy); }
  .brand-name {
    font-family: "Source Sans 3", sans-serif; font-weight: 700; font-size: 17px;
    color: var(--navy); line-height: 1.1; width: 170px;
  }
  .greeting {
    position: absolute; left: 54px; top: 208px;
    font-family: "Arimo", sans-serif; font-weight: 700; font-size: 16px; color: var(--heading);
  }
  .letter-body { position: absolute; left: 55px; top: 250px; width: 610px; }
  .letter-body p {
    font-family: "Source Sans 3", sans-serif; font-size: 15.2px; line-height: 18.9px;
    color: var(--text); text-align: justify; margin-bottom: 19px;
  }
  .signature {
    position: absolute; left: 64px; top: 668px; width: 118px; height: 60px;
    background: linear-gradient(90deg, #e4e4e4, #ececec);
  }
  .contact-strip { position: absolute; left: 0; top: 925px; width: 720px; height: 64px; }
  .contact-col {
    position: absolute; top: 0; width: 180px; text-align: center;
    font-family: "Roboto", sans-serif; font-size: 12px; line-height: 19.5px; color: var(--ink);
  }
  .contact-col svg { display: block; margin: 0 auto 3px; }
  .contact-col.address { left: 74px; font-family: "Roboto Condensed", sans-serif; font-size: 12.5px; }
  .contact-col.phone { left: 270px; }
  .contact-col.web { left: 476px; }
  .contact-col b { color: var(--navy); font-weight: 700; }
  .divider { position: absolute; top: 2px; width: 1px; height: 59px; background: var(--divider); }
  .divider.first { left: 269px; }
  .divider.second { left: 452px; }
  .tagline-band {
    position: absolute; left: 0; bottom: 0; width: 720px; height: 23px; background: var(--navy);
    color: #fff; font-family: "Lustria", serif; font-size: 11px; line-height: 23px; text-align: center;
  }
  .tagline-band .sep { margin: 0 6px; }
</style>
</head>
<body>
<main class="sheet">
  <svg class="header-wave" viewBox="0 0 720 60" aria-hidden="true">
    <path d="M0 0 H720 V56 C560 28 300 10 0 10 Z" fill="var(--navy)"/>
    <path d="M0 15 C300 8 560 25 720 58 C560 32 300 20 0 26 Z" fill="var(--orange)"/>
  </svg>

  <div class="brand">
    <div class="brand-square"></div>
    <div class="brand-name">Quarrybell Computer Services</div>
  </div>

  <h1 class="greeting">Dear Mr. Ellery,</h1>

  <section class="letter-body">
    <p>Lorem Ipsum is simply dummy text of the printing and typesetting industry. Lorem Ipsum has been the industry's standard dummy text ever since the 1500s, when an unknown printer took a galley of type and scrambled it to make a type specimen book. It has survived not only five centuries, but also the leap into electronic typesetting, remaining essentially unchanged.</p>
    <p>The standard chunk of Lorem Ipsum used since the 1500s is reproduced below for those interested. Sections 1.10.32 and 1.10.33 from "de Finibus Bonorum et Malorum" by Aemilius are also reproduced in their exact original form, accompanied by English versions from the 1914 translation by H. Marlowe</p>
    <p>Lorem Ipsum is simply dummy text of the printing and typesetting industry. Lorem Ipsum has been the industry's standard dummy text ever since the 1500s, when an unknown printer took a galley of type and scrambled it to make a type specimen book. It has survived not only five centuries, but also the leap into electronic typesetting, remaining essentially unchanged. It was popularised in the</p>
    <p>The standard chunk of Lorem Ipsum used since the 1500s is reproduced below for those interested. Sections 1.10.32 and 1.10.33 from "de Finibus Bonorum et Malorum" by Aemilius are also reproduced in their exact original form, accompanied by English versions from the 1914 translation by H. Marlowe</p>
  </section>

  <div class="signature" role="img" aria-label="Handwritten signature of the sender"></div>

  <footer class="contact-strip">
    <div class="contact-col address">
      <svg width="14" height="18" viewBox="0 0 14 18" aria-hidden="true"><path d="M7 1a6 6 0 0 0-6 6c0 4.5 6 10 6 10s6-5.5 6-10a6 6 0 0 0-6-6z" fill="none" stroke="var(--navy)" stroke-width="2"/><circle cx="7" cy="7" r="2" fill="var(--navy)"/></svg>
      47 Fernhollow Road<br>Alderbrook, VT 05999
    </div>
    <div class="divider first"></div>
    <div class="contact-col phone">
      <svg width="18" height="18" viewBox="0 0 18 18" aria-hidden="true"><circle cx="9" cy="9" r="8" fill="none" stroke="var(--navy)" stroke-width="1.3"/><path d="M10.5 4.5 9 5.2c-1.4 2.2-2 4.6-1.7 7.2l1.5.8 1-1.8-1-.9c0-1.3.3-2.5.9-3.6l1.3-.2z" fill="var(--navy)"/></svg>
      <b>T:</b> 802-555-0147<br><b>F:</b> 802-555-0192
    </div>
    <div class="divider second"></div>
    <div class="contact-col web">
      <svg width="17" height="17" viewBox="0 0 17 17" aria-hidden="true"><g fill="none" stroke="var(--navy)" stroke-width="1.1"><circle cx="8.5" cy="8.5" r="7.5"/><ellipse cx="8.5" cy="8.5" rx="3.3" ry="7.5"/><path d="M1 8.5h15M2.2 4.7h12.6M2.2 12.3h12.6M8.5 1v15"/></g></svg>
      Info@Quarrybell.example<br>www.Quarrybell.example
    </div>
  </footer>

  <div class="tagline-band">Steady Support<span class="sep">|</span>Friendly Experts<span class="sep">|</span>Reliable Results</div>
</main>
</body>
</html>
```